Nutrition-Cooking Website

Hello!
I am in a need of a lovely looking website for my new nutrition practice. I am looking for something sleek, sophisticated, professional yet also welcoming.

Here is a current layout which can be tweaked or overhauled. I feel like the website is not quite what I want so thats why I need your help!!
http://tolvanfolio.example/RENATA-OSSLER-concept-15/

Two websites I like are: (layout similar to www.marquetta.example) or http://www.pernillavostraken.example

Here are the tabs for the website:
About Registered Dietitian Healthy Recipes Philanthropy Shop Features Contact Blog

Features for the Home page include:
Slideshow with 3 rotating updates (like www.marquetta.example)
Video Box (like www.marquetta.example)
Recent Recipes (like http://harrowfield7731.example)
Recent Posts (like http://harrowfield7731.example)
Food Knowledge Box- quick tidbits on laws on food (like www.marquetta.example- she has food wisdom)
Tried and True Benefits of Mediterranean Cuisine (like www.marquetta.example)
Picture of me with brief quote/bio (like www.bettinoruval.example)
Social media buttons

Color Scheme:
• I like the white with gold embroidery or the pretty bluish/purplish in the first pic would be awesome with the slight pink undertones (http://glossedtwirl.example/2012/10/quorvel-marigelle-collection-by-tansley/)
• Also like this goldish background- exotic/sophisticated- http://www.thewhirlingcook.example/Home.html
• Also like the rustic goldish look in the background like this-
ohttp://img.prentlo.example/vexomarks_rsvp_vintage_rustic_gold_swirls_invitation-p161658028764768924bebn6_400.jpg
o http://img.prentlo.example/vexomarks_ornamental_rustic_gold_swirls_invitation-p161776340110432961bvddb_400.jpg
• maybe can have the vines as grapes/olives
OPEN TO ALL DIFFERENT COLORS SCHEMES- whatever looks, clean, sophisticated and professional

Logo:
• Attached is the logo

Budget is flexible. If you think you can improve the website- please do so :)

Target Market(s)

health conscious individuals of all ages

Industry/Entity Type

Embroidery

Requirements
Must have
• clean and sharp look
professional looking
Should not have
• too much busyness

```html
<!DOCTYPE html>
<html lang="en">
<head>
<meta charset="utf-8">
<title>Renata Ossler RD</title>
<link href="https://fonts.googleapis.com/css2?family=Cinzel:wght@400;700&display=swap" rel="stylesheet">
<style>
:root{
  --gold:#dcb057;
  --gold-light:#e8c66f;
  --gold-dark:#c99a3e;
  --cream:#f1e7d3;
  --pink:#d95d82;
  --pink-soft:#f0a19f;
  --pink-title:#c8476c;
  --card:#fcefef;
  --white:#ffffff;
  --text:#5a4a3a;
  --muted:#fbf2dc;
}
*{margin:0;padding:0;box-sizing:border-box}
html,body{width:823px;height:1200px;overflow:hidden}
body{background:var(--gold);font-family:Arial,Helvetica,sans-serif;position:relative;color:var(--text)}
.abs{position:absolute}
.serif{font-family:'Cinzel',Georgia,serif}
.header{left:0;top:0;width:823px;height:76px;background:var(--cream);border-bottom:3px solid var(--gold-dark)}
.brand{left:90px;top:26px;font-size:21px;letter-spacing:1px;color:#3a2f2a}
.social{top:12px;width:17px;height:17px;border-radius:50%;background:var(--gold)}
.search{left:556px;top:44px;width:181px;height:22px;background:var(--white);border:1px solid #e2d6bd}
.search svg{position:absolute;right:6px;top:4px}
.nav{left:83px;top:96px;width:657px;height:29px;background:var(--pink);display:flex;align-items:center;border-top:3px solid #c44a6c}
.nav a{font-family:'Cinzel',Georgia,serif;color:var(--white);font-size:9.5px;text-decoration:none;padding:0 12px;height:100%;display:flex;align-items:center;border-right:1px solid #c44a6c;letter-spacing:.4px}
.nav a:last-child{border-right:none}
.slide{left:82px;top:142px;width:431px;height:231px;background:var(--pink-soft);border:3px solid var(--white)}
.photo{background:linear-gradient(160deg,#e9e3dc,#c7b19a)}
.slide .photo{left:4px;top:6px;width:220px;height:212px;border-radius:50% 50% 48% 52%;border:3px solid var(--gold-light)}
.slide h2{left:230px;top:40px;font-size:20px;font-weight:400;color:var(--pink-title);line-height:22px}
.slide p{left:230px;top:100px;width:190px;font-size:9px;line-height:11.6px;color:var(--white);text-align:justify}
.more{font-family:'Cinzel',Georgia,serif;font-size:9px;color:var(--pink-title);font-weight:700}
.dots{left:377px;top:210px;display:flex;gap:8px}
.dots span{width:7px;height:7px;border-radius:50%;background:var(--pink)}
.dots span.on{background:var(--gold-light);box-shadow:0 0 0 2px #f3d98e}
.welcome{left:529px;top:142px;width:211px;height:231px;background:var(--pink-soft);border:2px solid var(--white)}
.welcome h2{width:100%;text-align:center;top:4px;font-size:19px;font-weight:400;color:var(--pink-title);padding-bottom:6px;border-bottom:1px dashed #e07f8f}
.welcome .photo{left:14px;top:40px;width:160px;height:124px;border-radius:50%;border:3px solid var(--gold-light);background:linear-gradient(140deg,#6a8fcf,#3a2a24)}
.welcome p{left:5px;top:172px;width:200px;font-size:7.6px;line-height:10px;color:var(--white);text-align:justify}
.card{top:398px;width:206px;height:239px;background:var(--card)}
.card h3{width:100%;height:30px;background:var(--pink);color:var(--white);font-size:15px;font-weight:400;text-align:center;line-height:30px;letter-spacing:.6px}
.card .photo{left:9px;top:37px;width:187px;height:127px;background:linear-gradient(150deg,#f3f1ec,#8fae58 55%,#d9d2c4)}
.card h4,.feature h4{font-size:10.5px;font-weight:400;color:var(--pink-title);letter-spacing:.4px}
.card h4{left:8px;top:173px}
.card p{left:8px;top:194px;width:192px;font-size:7.6px;line-height:10.5px}
.card a{left:8px;top:221px;font-size:8px;color:#c9922e;text-decoration:none}
.feature{left:535px;top:398px;width:205px;height:239px;background:var(--gold-light)}
.feature .photo{left:0;top:0;width:205px;height:156px;background:linear-gradient(135deg,#aeb5bc,#4a4c50)}
.feature h4{left:8px;top:166px;color:var(--pink)}
.feature p{left:7px;top:186px;width:191px;font-size:7.6px;line-height:10px;text-align:justify}
.section-title{top:674px;width:322px;height:40px}
.section-title span{position:absolute;left:5px;top:14px;font-size:16px;color:var(--muted);letter-spacing:.6px}
.post{width:322px;height:90px}
.post .photo{left:0;top:0;width:117px;height:78px;border:3px solid var(--white)}
.post h5{left:130px;top:2px;font-family:'Cinzel',Georgia,serif;font-weight:400;font-size:10.5px;color:var(--muted);letter-spacing:.4px}
.post p{left:130px;top:24px;width:192px;font-size:8.5px;line-height:11.6px;color:var(--muted);text-align:justify}
.rule{height:1px;width:322px;background:#cda14c}
.newsletter{left:82px;top:1070px;width:659px;height:48px}
.newsletter h2{left:30px;top:14px;font-size:17px;font-weight:400;color:var(--white);letter-spacing:.5px}
.newsletter .email{left:309px;top:15px;width:212px;height:24px;background:var(--white);font-size:8px;padding:8px 7px;color:#555}
.newsletter .signup{left:536px;top:15px;width:68px;height:24px;background:#f7e3e7;color:var(--pink);font-weight:700;font-size:12px;text-align:center;line-height:24px}
.footer-rule{left:82px;top:1146px;width:659px;height:1px;background:#cda14c}
.footer{left:0;width:823px;top:1165px;text-align:center;font-size:9px;color:var(--muted)}
</style>
</head>
<body>
<header class="abs header">
  <div class="abs brand serif">RENATA OSSLER RD</div>
  <span class="abs social" style="left:653px"></span>
  <span class="abs social" style="left:674px"></span>
  <span class="abs social" style="left:695px"></span>
  <span class="abs social" style="left:716px"></span>
  <div class="abs search"><svg width="13" height="13" viewBox="0 0 13 13"><circle cx="5" cy="5" r="3.6" fill="none" stroke="#bbb" stroke-width="1.6"/><line x1="7.7" y1="7.7" x2="12" y2="12" stroke="#bbb" stroke-width="2"/></svg></div>
</header>

<nav class="abs nav">
  <a href="#">HOME</a><a href="#">ABOUT</a><a href="#">REGISTERED DIETITIAN</a><a href="#">HEALTH Y RECIPES</a><a href="#">PHILANTHROPY</a><a href="#">SHOP FEATURES</a><a href="#">CONTACT</a><a href="#">BLOG</a>
</nav>

<section class="abs slide">
  <div class="abs photo" role="img" aria-label="Scoop of roasted banana ice cream with whipped cream and a cherry in a glass bowl"></div>
  <h2 class="abs serif">ROASTED BANANA<br>ICE CREAM</h2>
  <p class="abs">This is the ultimate ice cream sundae. Obviously, if you're not a peanut-eater, it won't be for you, but for everyone else it is the stuff of dreams. Last time I made this sauce, I nearly had to make...</p>
  <div class="abs more" style="left:230px;top:180px">SEE RECIPE ▸</div>
  <div class="abs dots"><span class="on"></span><span></span><span></span></div>
</section>

<aside class="abs welcome">
  <h2 class="abs serif">WELCOME</h2>
  <div class="abs photo" role="img" aria-label="Portrait photo of the dietitian"></div>
  <p class="abs">consectetur adipisicing elit, sed do eiusmod tempor incididunt ut labore et dolore magna aliqua. Ut enim ad minim veniam,</p>
  <div class="abs more" style="left:5px;top:213px">READ MORE ▸</div>
</aside>

<article class="abs card" style="left:82px">
  <h3 class="serif">FOOD KNOWLEDGE</h3>
  <div class="abs photo" role="img" aria-label="Fresh salad on a white plate"></div>
  <h4 class="abs serif">SED UT PERSPICIATIS UNDE</h4>
  <p class="abs">There are a few meals I can say I'm making that will make...</p>
  <a class="abs" href="#">Read More</a>
</article>
<article class="abs card" style="left:309px">
  <h3 class="serif">FOOD PHILOSOPHY</h3>
  <div class="abs photo" role="img" aria-label="Fresh salad on a white plate"></div>
  <h4 class="abs serif">SED UT PERSPICIATIS UNDE</h4>
  <p class="abs">There are a few meals I can say I'm making that will make...</p>
  <a class="abs" href="#">Read More</a>
</article>
<article class="abs feature">
  <div class="abs photo" role="img" aria-label="Video still of the dietitian in a kitchen"></div>
  <h4 class="abs serif">SED UT PERSPICIATIS UNDE</h4>
  <p class="abs">voluptatem accusantium doloremque laudantium, totam rem aperiam, eaque ipsa quae ab illo inventore veritatis et quasi architecto beatae vitae dicta sunt explicabo.</p>
</article>

<div class="abs section-title" style="left:82px">
  <svg width="322" height="40" viewBox="0 0 322 40"><polygon points="0,0 322,14 322,40 0,40" fill="var(--gold-light)"/><polygon points="0,0 322,14 322,19 0,5" fill="var(--gold-dark)"/></svg>
  <span class="serif">RECENT POSTS</span>
</div>
<div class="abs section-title" style="left:418px">
  <svg width="322" height="40" viewBox="0 0 322 40"><polygon points="0,0 322,14 322,40 0,40" fill="var(--gold-light)"/><polygon points="0,0 322,14 322,19 0,5" fill="var(--gold-dark)"/></svg>
  <span class="serif">RECENT RECIPES</span>
</div>

<div class="abs post" style="left:82px;top:737px"><div class="abs photo" role="img" aria-label="Seafood platter with olives" style="background:linear-gradient(135deg,#b5502a,#6d7a2e,#d8c9a8)"></div><h5 class="abs">SPRING AWAKENING</h5><p class="abs">perspiciatis unde omnis iste natus error sit voluptatem accusantium doloremque laudan-tium, totam rem aperiam,eaque ipsa quae ab illo inventore veritatis et quasi</p></div>
<div class="abs rule" style="left:82px;top:830px"></div>
<div class="abs post" style="left:82px;top:842px"><div class="abs photo" role="img" aria-label="Fried egg with tomatoes and greens" style="background:linear-gradient(135deg,#9a5a3a,#f4f0e6,#6a9a3a)"></div><h5 class="abs">SPRING AWAKENING</h5><p class="abs">perspiciatis unde omnis iste natus error sit voluptatem accusantium doloremque laudan-tium, totam rem aperiam,eaque ipsa quae ab illo inventore veritatis et quasi</p></div>
<div class="abs rule" style="left:82px;top:936px"></div>
<div class="abs post" style="left:82px;top:948px"><div class="abs photo" role="img" aria-label="Baguette sandwich with tomato and egg" style="background:linear-gradient(135deg,#c98a4a,#e04a3a,#f3efe6)"></div><h5 class="abs">SPRING AWAKENING</h5><p class="abs">perspiciatis unde omnis iste natus error sit voluptatem accusantium doloremque laudan-tium, totam rem aperiam,eaque ipsa quae ab illo inventore veritatis et quasi</p></div>
<div class="abs rule" style="left:82px;top:1042px"></div>

<div class="abs post" style="left:418px;top:737px"><div class="abs photo" role="img" aria-label="Stir-fried chicken and vegetables" style="background:linear-gradient(135deg,#f2ece2,#d8822e,#b8532a)"></div><h5 class="abs">SPRING AWAKENING</h5><p class="abs">perspiciatis unde omnis iste natus error sit voluptatem accusantium doloremque laudan-tium, totam rem aperiam,eaque ipsa quae ab illo inventore veritatis et quasi</p></div>
<div class="abs rule" style="left:418px;top:830px"></div>
<div class="abs post" style="left:418px;top:842px"><div class="abs photo" role="img" aria-label="Collage of fried chicken, pasta and a burger" style="background:linear-gradient(135deg,#b0601e,#d63a2a,#e8dcc4)"></div><h5 class="abs">SPRING AWAKENING</h5><p class="abs">perspiciatis unde omnis iste natus error sit voluptatem accusantium doloremque laudan-tium, totam rem aperiam,eaque ipsa quae ab illo inventore veritatis et quasi</p></div>
<div class="abs rule" style="left:418px;top:936px"></div>
<div class="abs post" style="left:418px;top:948px"><div class="abs photo" role="img" aria-label="Basket of fresh vegetables" style="background:linear-gradient(135deg,#3f7a2a,#d8332a,#f0c03a)"></div><h5 class="abs">SPRING AWAKENING</h5><p class="abs">perspiciatis unde omnis iste natus error sit voluptatem accusantium doloremque laudan-tium, totam rem aperiam,eaque ipsa quae ab illo inventore veritatis et quasi</p></div>
<div class="abs rule" style="left:418px;top:1042px"></div>

<section class="abs newsletter">
  <svg class="abs" width="659" height="48" viewBox="0 0 659 48" style="left:0;top:0"><polygon points="0,0 659,7 659,48 0,48" fill="var(--pink)"/><line x1="0" y1="46.5" x2="659" y2="46.5" stroke="#b8405f" stroke-width="2"/></svg>
  <h2 class="abs serif">JOIN RENATA'S NEWSLETTER</h2>
  <div class="abs email">Enter your Email</div>
  <div class="abs signup">SIGNUP</div>
</section>

<div class="abs footer-rule"></div>
<footer class="abs footer">© 2013 Renata Ossler | All Rights Reserved</footer>
</body>
</html>
```